Need design for Vinyl window signs

I need Vinyl window sign to cover my front retail pharmacy window. Not the whole window area i want there to be open areas so people can still see inside.
Attached is the pic of front door and also the logo which contains the colors we want to use. The width of the door is about 14ft wide and 7ft high and its 3 sections. The middle section the door is 36 inch.

And the vinyl graphic should include the following info:
Ellerby Grove pharmacy
Caring for you, Caring for the community

Wellness starts here!
Locally owned independent pharmacy
No wait
Same Copay as chains
Free local delivery

We do prescriptions, private consultations, compounding, immunizations, travel health and other clinical services

We also provide free blood pressure, blood glucose and blood oxygen testing everyday.
No appointments necessary.

Write Pharmacy in different languages: Spanish, Farsi, Hebrew, Russian

Phone: 555-286-4907

Hours:
M- F 9-6
Sat and sun and major Holliday: closed

Target Market(s)

Patients: People seeking medication or health advice. Caregivers: Those caring for others who need prescriptions. Health-Conscious Individuals: People interested in preventive health measures. Chronic Condition Sufferers: Individuals managing ongoing health issues. Healthcare Professionals: Doctors and nurses who may refer patients to pharmacists.

Industry/Entity Type

Retail pharmacy

Font styles to use
Sans Serif

Colors
0054AA
0677BA
7BADD7
CADEEF
E8F1F8
00AB8E
00BBA5
67D7C9
C6EFE9
E9F9F6

Requirements
Must have
• At least 3 sections for each window left side and right side and middle area, must have Green and blue color to match my logo see attached.
Nice to have
• Like to see a pics or two of people maybe seniors and younger adults enjoying their time

```html
<!DOCTYPE html>
<html lang="en">
<head>
<meta charset="utf-8">
<title>Ellerby Grove pharmacy – window vinyl set</title>
<link href="https://fonts.googleapis.com/css2?family=Montserrat:wght@500;600;700;800&display=swap" rel="stylesheet">
<style>
  :root {
    --green: #00a94f;
    --blue: #0a62b8;
    --blue-deep: #0054aa;
    --white: #ffffff;
    --backdrop: #cfcfcf;
    --photo-light: #eef1f3;
    --photo-mid: #c9d3da;
  }
  * { margin: 0; padding: 0; box-sizing: border-box; }
  html, body { width: 1200px; height: 1080px; overflow: hidden; }
  body {
    background: var(--backdrop);
    font-family: "Montserrat", sans-serif;
    color: var(--white);
    position: relative;
  }
  .window-set {
    position: absolute;
    top: 394px;
    left: 28px;
    display: flex;
    gap: 10px;
  }
  .panel {
    position: relative;
    height: 292px;
    overflow: hidden;
    background: var(--white);
  }
  .panel svg.panel-shapes {
    position: absolute;
    inset: 0;
    width: 100%;
    height: 100%;
  }
  .photo { position: absolute; }

  /* Left panel */
  .panel--welcome { width: 443px; }
  .panel--welcome .photo {
    top: 0; right: 0; width: 260px; height: 100%;
    background: linear-gradient(160deg, var(--photo-light) 0%, var(--photo-mid) 60%, #e8d7c8 100%);
  }
  .welcome-text {
    position: absolute;
    top: 18px;
    left: 43px;
    width: 300px;
  }
  .brand-line { font-weight: 700; font-size: 21px; line-height: 1; }
  .brand-word { font-weight: 800; font-size: 45px; line-height: 0.95; letter-spacing: -0.5px; }
  .tagline { font-weight: 600; font-size: 14.5px; line-height: 1.2; margin-top: 8px; }
  .pill {
    display: inline-block;
    background: var(--blue);
    border-radius: 20px;
    font-weight: 700;
    white-space: nowrap;
  }
  .welcome-text .pill { font-size: 15px; padding: 3px 10px; margin-top: 14px; }
  .checks { list-style: none; margin-top: 6px; }
  .checks li {
    font-size: 9.2px; font-weight: 600; line-height: 15.5px;
    display: flex; align-items: center; gap: 7px;
  }
  .checks svg { width: 8px; height: 8px; flex: none; }

  /* Middle panel */
  .panel--contact { width: 243px; }
  .brand-mark {
    position: absolute;
    top: 8px; left: 0; width: 100%;
    display: flex; flex-direction: column; align-items: center; gap: 4px;
  }
  .brand-mark .dot {
    width: 80px; height: 80px; border-radius: 50%;
    background: var(--green);
    border: 6px solid var(--blue);
  }
  .brand-mark .name { color: var(--green); font-weight: 800; font-size: 15px; line-height: 1.1; }
  .phone {
    position: absolute; top: 146px; left: 0; width: 100%;
    display: flex; justify-content: center; align-items: center; gap: 6px;
    font-weight: 700; font-size: 23px;
  }
  .phone svg { width: 18px; height: 18px; }
  .hours {
    position: absolute; top: 190px; left: 0; width: 100%;
    text-align: center;
  }
  .hours h2 { font-weight: 800; font-size: 19px; }
  .hours .pill {
    font-size: 10.5px; font-weight: 600; padding: 3px 10px; margin-top: 6px;
    border: 1.5px solid var(--white); background: transparent;
  }
  .hours p { font-size: 10.5px; font-weight: 600; line-height: 1.25; margin-top: 9px; }

  /* Right panel */
  .panel--services { width: 444px; }
  .panel--services .photo {
    top: 0; left: 0; width: 100%; height: 100%;
    background: linear-gradient(200deg, var(--photo-light) 0%, var(--photo-mid) 55%, #f4f4f4 100%);
  }
  .services {
    position: absolute; top: 16px; left: 262px; list-style: none;
  }
  .services li {
    font-size: 11px; font-weight: 600; line-height: 1.1; margin-bottom: 10.5px;
    display: flex; gap: 8px;
  }
  .services li svg { width: 6px; height: 7px; flex: none; margin-top: 3px; }
  .no-appointments {
    position: absolute; top: 149px; left: 256px; right: 0;
    background: var(--blue);
    border-radius: 12px 0 0 12px;
    font-size: 9.5px; font-weight: 700; padding: 4px 0 4px 12px;
  }
  .free-testing {
    position: absolute; top: 175px; right: 22px; width: 150px;
    text-align: right; font-size: 9.5px; font-weight: 600; line-height: 1.25;
  }
</style>
</head>
<body>
<main class="window-set">

  <section class="panel panel--welcome">
    <div class="photo" role="img" aria-label="Photo of a pharmacist in a white coat holding a medicine bottle and a tablet"></div>
    <svg class="panel-shapes" viewBox="0 0 720 476" preserveAspectRatio="none" aria-hidden="true">
      <path d="M0,0 H690 C620,140 600,330 430,420 C300,480 120,480 0,470 V476 H0 Z" fill="var(--blue)"/>
      <path d="M0,0 H655 C590,140 570,310 410,385 C290,440 120,445 0,430 Z" fill="var(--white)"/>
      <path d="M0,0 H620 C560,140 540,290 390,360 C280,410 120,415 0,395 Z" fill="var(--green)"/>
    </svg>
    <div class="welcome-text">
      <div class="brand-line">Ellerby Grove</div>
      <div class="brand-word">pharmacy</div>
      <p class="tagline">Caring for you, Caring for<br>the community</p>
      <div class="pill">Wellness starts here!</div>
      <ul class="checks">
        <li><svg viewBox="0 0 10 10"><circle cx="5" cy="5" r="5" fill="#fff"/><path d="M2.6,5.2 4.3,6.8 7.4,3.6" stroke="var(--green)" stroke-width="1.6" fill="none"/></svg>Locally owned independent pharmacy</li>
        <li><svg viewBox="0 0 10 10"><circle cx="5" cy="5" r="5" fill="#fff"/><path d="M2.6,5.2 4.3,6.8 7.4,3.6" stroke="var(--green)" stroke-width="1.6" fill="none"/></svg>No wait</li>
        <li><svg viewBox="0 0 10 10"><circle cx="5" cy="5" r="5" fill="#fff"/><path d="M2.6,5.2 4.3,6.8 7.4,3.6" stroke="var(--green)" stroke-width="1.6" fill="none"/></svg>Same Copay as chains</li>
        <li><svg viewBox="0 0 10 10"><circle cx="5" cy="5" r="5" fill="#fff"/><path d="M2.6,5.2 4.3,6.8 7.4,3.6" stroke="var(--green)" stroke-width="1.6" fill="none"/></svg>Free local delivery</li>
      </ul>
    </div>
  </section>

  <section class="panel panel--contact">
    <svg class="panel-shapes" viewBox="0 0 243 292" preserveAspectRatio="none" aria-hidden="true">
      <path d="M0,138 C70,122 170,122 243,130 V292 H0 Z" fill="var(--green)"/>
      <path d="M0,199 C70,178 170,178 243,195 V292 H0 Z" fill="var(--white)"/>
      <path d="M0,203 C70,182 170,182 243,199 V292 H0 Z" fill="var(--blue)"/>
    </svg>
    <div class="brand-mark">
      <div class="dot"></div>
      <div class="name">Ellerby Grove</div>
    </div>
    <div class="phone">
      <svg viewBox="0 0 20 20"><circle cx="10" cy="10" r="10" fill="#fff"/><path d="M6.5,5 8.5,4.8 9.6,7.6 8.4,8.6 C9,10 10,11 11.4,11.6 L12.4,10.4 15.2,11.5 15,13.5 C11,14.4 5.6,9 6.5,5 Z" fill="var(--green)"/></svg>
      555-286-4907
    </div>
    <div class="hours">
      <h2>HOURS:</h2>
      <div class="pill">Monday - Friday 9AM-6PM</div>
      <p>Sat and sun and<br>major Holliday: closed</p>
    </div>
  </section>

  <section class="panel panel--services">
    <div class="photo" role="img" aria-label="Photo of a smiling pharmacist in a white uniform with arms crossed"></div>
    <svg class="panel-shapes" viewBox="0 0 444 292" preserveAspectRatio="none" aria-hidden="true">
      <path d="M164,0 H444 V292 H430 C300,285 200,210 178,110 C170,70 166,35 164,0 Z" fill="var(--blue)"/>
      <path d="M188,0 H444 V274 H425 C310,268 225,200 200,110 C194,75 190,40 188,0 Z" fill="var(--white)"/>
      <path d="M203,0 H444 V258 H420 C320,250 240,190 215,110 C208,80 205,40 203,0 Z" fill="var(--green)"/>
    </svg>
    <ul class="services">
      <li><svg viewBox="0 0 6 7"><path d="M0,0 6,3.5 0,7Z" fill="#fff"/></svg>We do prescriptions</li>
      <li><svg viewBox="0 0 6 7"><path d="M0,0 6,3.5 0,7Z" fill="#fff"/></svg>private consultations</li>
      <li><svg viewBox="0 0 6 7"><path d="M0,0 6,3.5 0,7Z" fill="#fff"/></svg>compounding</li>
      <li><svg viewBox="0 0 6 7"><path d="M0,0 6,3.5 0,7Z" fill="#fff"/></svg>immunizations,</li>
      <li><svg viewBox="0 0 6 7"><path d="M0,0 6,3.5 0,7Z" fill="#fff"/></svg>travel health and other<br>clinical services</li>
    </ul>
    <div class="no-appointments">No appointments necessary</div>
    <p class="free-testing">We also provide free<br>blood pressure • blood<br>glucose and blood<br>oxygen testing<br>everyday.</p>
  </section>

</main>
</body>
</html>
```